Postcard Design

Maple Ledger Inc.
Title of service: "Ward Wagon" - mobile scrub uniform store, where we go to nursing homes and employees buy their uniforms through us

Photos to consider: nurses, aides, people who work in nursing homes.

need a postcard design for direct mailing nursing homes to promote our traveling nursing uniform store to nursing homes
Contact details:
Email (will provide email to winner only)
Phone 18004729316

Points of Interest to Mention on Card:
Family-Owned Business, Providing impeccable service since 1975
Large Inventory
Stock includes Halvorn, Pellway Brands, budget brands
Reduced Prices
Will work with your schedule to fit your needs
Designated stock colors for your department staff
Special order items are available
150+ top choices per size (XXS-5XL)

Target Market(s)

Director of nursing, nursing homes staff

Industry/Entity Type

Store

```html
<!DOCTYPE html>
<html lang="en">
<head>
<meta charset="utf-8">
<title>Ward Wagon Postcard</title>
<link href="https://fonts.googleapis.com/css2?family=Oswald:wght@500;700&family=Open+Sans:wght@400;600;700&family=PT+Serif&display=swap" rel="stylesheet">
<style>
  :root {
    --backdrop: #e9ebee;
    --sky-light: #cfeefa;
    --sky: #7cc6ec;
    --sky-deep: #3ea4dc;
    --title-blue: #2f8fd6;
    --navy: #1d5fa0;
    --lime-light: #c6dc62;
    --lime: #9dbb3b;
    --lime-deep: #7f9e2a;
    --ink: #1b1b1b;
    --paper: #ffffff;
    --rule: #333333;
    --photo-a: #cfe0e4;
    --photo-b: #3fa4b4;
    --photo-c: #5a78b8;
  }
  * { box-sizing: border-box; margin: 0; padding: 0; }
  html, body { width: 900px; height: 1200px; overflow: hidden; }
  body { background: var(--backdrop); position: relative; font-family: "Open Sans", sans-serif; }

  .postcard { position: absolute; box-shadow: 0 4px 14px rgba(0,0,0,.25); }

  /* Front */
  .postcard--front { left: 118px; top: 55px; width: 665px; height: 505px; overflow: hidden;
    background: linear-gradient(180deg, var(--sky-light) 0%, var(--sky) 70%, var(--sky-deep) 100%); }
  .front-art { position: absolute; inset: 0; }
  .brand-title { position: absolute; left: 60px; top: 38px; font-family: "Oswald", sans-serif; font-weight: 700;
    font-size: 92px; line-height: 94px; letter-spacing: 1px; }
  .brand-title .line-one { display: block; color: var(--lime); }
  .brand-title .line-two { display: block; color: var(--title-blue); }
  .call-box { position: absolute; left: 87px; top: 263px; width: 205px; height: 44px;
    background: linear-gradient(90deg, var(--lime-deep), var(--lime)); display: flex; align-items: center;
    justify-content: center; gap: 6px; font-family: "Oswald", sans-serif; color: #fff; box-shadow: 0 3px 6px rgba(0,0,0,.25); }
  .call-box .label { font-size: 17px; font-weight: 500; }
  .call-box .number { font-size: 23px; font-weight: 500; color: #1a1a1a; }
  .pitch-box { position: absolute; left: 20px; top: 335px; width: 272px; height: 107px;
    background: linear-gradient(90deg, var(--lime-deep), var(--lime-light)); padding: 16px 16px;
    font-size: 14.5px; line-height: 19.5px; color: #1a1a1a; box-shadow: 0 3px 6px rgba(0,0,0,.25); }

  /* Back */
  .postcard--back { left: 118px; top: 610px; width: 670px; height: 515px; background: var(--paper); }
  .info-panel { position: absolute; left: 22px; top: 18px; width: 390px; height: 472px;
    background: linear-gradient(180deg, #e4f4fb 0%, var(--sky) 75%, var(--sky-deep) 100%); }
  .ribbon { position: absolute; left: 15px; width: 408px; background: linear-gradient(180deg, var(--lime-light), var(--lime) 60%, var(--lime-deep));
    box-shadow: 0 4px 6px rgba(0,0,0,.2); }
  .ribbon--heritage { top: 50px; height: 85px; text-align: center; padding-top: 13px; }
  .ribbon--heritage .tagline { font-size: 12.5px; font-weight: 700; color: var(--ink); }
  .ribbon--heritage .since { font-size: 32px; font-weight: 700; color: var(--navy); line-height: 44px; }
  .section-tag { position: absolute; left: 22px; top: 160px; width: 390px; height: 36px; }
  .section-tag span { position: absolute; left: 0; right: 0; top: 6px; text-align: center; font-family: "PT Serif", serif; font-size: 22px; color: var(--ink); }
  .about-text { position: absolute; left: 52px; top: 205px; width: 348px; font-size: 14.5px; line-height: 18.5px;
    text-align: justify; color: var(--ink); }
  .about-rule { position: absolute; left: 55px; top: 290px; width: 338px; height: 2px; background: var(--ink); }
  .about-more { position: absolute; left: 55px; top: 298px; font-size: 14px; line-height: 19px; color: var(--ink); }
  .ribbon--contact { top: 375px; height: 87px; padding: 10px 0 0 35px; }
  .contact-row { display: flex; align-items: center; gap: 14px; height: 24px; font-size: 15px; font-weight: 600; color: var(--ink); }
  .contact-row svg { width: 14px; height: 14px; fill: var(--navy); }
  .contact-mark { position: absolute; right: 30px; top: 10px; font-family: "Oswald", sans-serif; font-weight: 700;
    font-size: 30px; line-height: 32px; color: rgba(255,255,255,.35); text-align: center; }
  .stamp-box { position: absolute; left: 575px; top: 90px; width: 62px; height: 67px; border: 1px solid #777; }
  .address-line { position: absolute; left: 454px; width: 183px; height: 1px; background: var(--rule); }
</style>
</head>
<body>

<section class="postcard postcard--front">
  <svg class="front-art" width="665" height="505" viewBox="0 0 665 505">
    <defs>
      <linearGradient id="photoTone" x1="0" y1="0" x2="1" y2="1">
        <stop offset="0" stop-color="var(--photo-a)"/>
        <stop offset="0.55" stop-color="var(--photo-b)"/>
        <stop offset="1" stop-color="var(--photo-c)"/>
      </linearGradient>
    </defs>
    <polygon points="440,0 665,0 665,505 225,505" fill="var(--lime)"/>
    <polygon role="img" aria-label="Photo of a medical team in scrubs, caps and masks at work" points="448,0 665,0 665,505 236,505" fill="url(#photoTone)"/>
  </svg>
  <h1 class="brand-title"><span class="line-one">WARD</span><span class="line-two">WAGON</span></h1>
  <div class="call-box"><span class="label">CALL US :</span><span class="number">18004729316</span></div>
  <p class="pitch-box">Mobile scrub uniform store, where we go to nursing homes and employees buy their uniforms through us</p>
</section>

<section class="postcard postcard--back">
  <div class="info-panel"></div>
  <div class="ribbon ribbon--heritage">
    <p class="tagline">Family-Owned Business, Providing impeccable service</p>
    <p class="since">since 1975</p>
  </div>
  <div class="section-tag">
    <svg width="390" height="36" viewBox="0 0 390 36">
      <line x1="20" y1="18" x2="370" y2="18" stroke="var(--lime)" stroke-width="2"/>
      <polygon points="118,18 134,0 256,0 272,18 256,36 134,36" fill="var(--lime-light)"/>
    </svg>
    <span>ABOUT US</span>
  </div>
  <p class="about-text">Large Inventory Stock includes Halvorn, Pellway Brands, budget brands. Will work with your schedule to fit your needs Designated stock colors for your department staff Special</p>
  <div class="about-rule"></div>
  <p class="about-more">order items are available<br>150+ top choices per size (XXS-5XL).</p>
  <div class="ribbon ribbon--contact">
    <div class="contact-row"><svg viewBox="0 0 24 24"><path d="M6.6 10.8a15.1 15.1 0 0 0 6.6 6.6l2.2-2.2c.3-.3.7-.4 1-.2 1.1.4 2.3.6 3.6.6.6 0 1 .4 1 1V20c0 .6-.4 1-1 1A17 17 0 0 1 3 4c0-.6.4-1 1-1h3.5c.6 0 1 .4 1 1 0 1.3.2 2.5.6 3.6.1.3 0 .7-.2 1z"/></svg>18004729316</div>
    <div class="contact-row"><svg viewBox="0 0 24 24"><path d="M12 3 2 12h3v9h5v-6h4v6h5v-9h3z"/></svg>your address</div>
    <div class="contact-row"><svg viewBox="0 0 24 24"><path d="M2 5h20v14H2z M2 5l10 8 10-8" /></svg>your email address</div>
    <div class="contact-mark">WARD<br>WAGON</div>
  </div>
  <div class="stamp-box"></div>
  <div class="address-line" style="top:256px"></div>
  <div class="address-line" style="top:287px"></div>
  <div class="address-line" style="top:318px"></div>
</section>

</body>
</html>
```